I am looking for business cards and letterhead

I want a high-level look for CEO's who want a concierge level leadership consultant and organization development strategist

This needs to go with my brand: simple, elegant, clean. Please improve on this design while using these fonts and colors

Here is my website: CorinneHalvers.com

```html
<!DOCTYPE html>
<html lang="en">
<head>
<meta charset="UTF-8">
<title>Corinne Halvers — Business Card</title>
<link href="https://fonts.googleapis.com/css2?family=Tinos:wght@400;700&display=swap" rel="stylesheet">
<style>
  :root {
    --navy: #0a1433;
    --blue: #1a5fb4;
    --gold: #e6c88a;
    --white: #f4f4f4;
    --backdrop: #1c1c1c;
  }
  * { margin: 0; padding: 0; box-sizing: border-box; }
  html, body { width: 1200px; height: 1059px; overflow: hidden; }
  body {
    background: var(--backdrop);
    font-family: "Tinos", "Times New Roman", serif;
    position: relative;
  }
  .card {
    position: absolute;
    left: 252px;
    width: 700px;
    height: 400px;
    background: var(--navy);
    border-radius: 24px;
    overflow: hidden;
    color: var(--white);
  }
  .card--front { top: 98px; }
  .card--back { top: 552px; }

  .brand-mark {
    position: absolute;
    border: 4px solid var(--gold);
    border-radius: 50%;
    display: flex;
    align-items: center;
    justify-content: center;
    text-align: center;
    color: var(--white);
    font-weight: 700;
    line-height: 1.15;
  }
  .card--front .brand-mark {
    left: 489px; top: 33px; width: 168px; height: 168px;
    font-size: 19px;
  }
  .card--back .brand-mark {
    left: 236px; top: 86px; width: 229px; height: 229px;
    font-size: 26px;
  }

  .holder-name {
    position: absolute; left: 36px; top: 184px;
    font-size: 27px; font-weight: 700; color: var(--blue);
  }
  .holder-role {
    position: absolute; left: 35px; top: 224px;
    font-size: 18px;
  }
  .divider {
    position: absolute; left: 35px; top: 266px;
    width: 630px; height: 1.5px; background: var(--white);
  }
  .contact-list {
    position: absolute; left: 34px; top: 280px;
    list-style: none; font-size: 18px;
  }
  .contact-list li {
    display: flex; align-items: center; gap: 10px;
    height: 32px;
  }
  .contact-list svg { width: 18px; height: 18px; fill: var(--gold); }
  .address {
    position: absolute; right: 35px; top: 288px;
    text-align: right; font-size: 18px; line-height: 25px;
    font-style: normal;
  }
  .band { position: absolute; left: 0; top: 0; width: 700px; height: 400px; }
  .website {
    position: absolute; left: 440px; width: 250px; top: 370px;
    text-align: center; font-size: 18px; color: var(--navy);
  }
</style>
</head>
<body>

<section class="card card--front">
  <div class="brand-mark">Halvers<br>Advisory</div>

  <h1 class="holder-name">Corinne Halvers</h1>
  <p class="holder-role">Owner</p>
  <div class="divider"></div>

  <ul class="contact-list">
    <li>
      <svg viewBox="0 0 24 24" aria-hidden="true"><path d="M6.6 10.8a15.1 15.1 0 0 0 6.6 6.6l2.2-2.2a1 1 0 0 1 1-.25 11.4 11.4 0 0 0 3.6.57 1 1 0 0 1 1 1V20a1 1 0 0 1-1 1A17 17 0 0 1 3 4a1 1 0 0 1 1-1h3.5a1 1 0 0 1 1 1c0 1.25.2 2.45.57 3.57a1 1 0 0 1-.25 1z"/></svg>
      (407) 555-0142
    </li>
    <li>
      <svg viewBox="0 0 24 24" aria-hidden="true"><path d="M2 5h20v14H2z M2 5l10 8 10-8" fill="var(--gold)"/><path d="M2 5l10 8 10-8" fill="none" stroke="var(--navy)" stroke-width="1.6"/></svg>
      info@corinnehalvers.com
    </li>
  </ul>

  <address class="address">18 Willow Crest Lane<br>32801, United States</address>

  <svg class="band" viewBox="0 0 700 400" aria-hidden="true">
    <path d="M0 366 L420 366 C410 372 402 379 390 380 L0 380 Z" fill="var(--blue)"/>
    <path d="M0 383 L395 383 C420 383 425 360 452 360 L700 360 L700 400 L0 400 Z" fill="var(--gold)"/>
  </svg>
  <p class="website">www.corinnehalvers.com</p>
</section>

<section class="card card--back">
  <div class="brand-mark">Halvers<br>Advisory</div>
</section>

</body>
</html>
```